General Contractors need a new Crisp updated Card Design

We need a new business card design for our company of 25 years based in Toronto call Holvaster Building Inc. : Our goal is to be the leading commercial contractors in Toronto by providing exceptional value to our clients. We work very hard to deliver professional, quality, service in conjunction with consistent price competitiveness to all of our clients on every single project.

Target Market(s)

Design & Build Clients

Industry/Entity Type

Construction Company

Contact Information for Business Card

Address:
18 North Tamlin Glen Road, Unit 57, Marbrook Vale, ON, K7T 2R9
Office: 905-218-5937

Holvasters Logo
Employee Job Description
Employee Cell Phone #
Employee Email
www.holvaster-example.com

Colors

Designer to choose colors to be used in the design.

Requirements
Must have
• Quote Company Saying:
• "Professional. Quality. Service."
Nice to have
• New Crisp up to date look. simple & fresh ( Not to Busy)
Should not have
• NO BLUE PRINTS ON THE BUSINESS CARDS

```html
<!DOCTYPE html>
<html lang="en">
<head>
<meta charset="utf-8">
<title>Holvaster Building Inc. – Business Card</title>
<link rel="stylesheet" href="https://fonts.googleapis.com/css2?family=EB+Garamond:wght@400;500;600&family=Lato:wght@400&display=swap">
<style>
  :root{
    --teal:#006c66;
    --sage:#aec8bc;
    --white:#ffffff;
    --backdrop:#dcdcdc;
  }
  *{box-sizing:border-box;margin:0;padding:0}
  html,body{width:1200px;height:900px;overflow:hidden}
  body{background:var(--backdrop);position:relative;font-family:'Lato',sans-serif}
  .card{position:absolute;left:305px;width:590px;height:343px;background:var(--white);border-radius:28px;overflow:hidden;box-shadow:0 4px 10px rgba(0,0,0,.18)}
  .card--front{top:80px}
  .card--back{top:478px}

  .brand{position:absolute;display:flex;align-items:center;gap:16px}
  .brand__mark{width:82px;height:82px;background:var(--teal);flex:none}
  .brand__name{font-family:'EB Garamond',serif;font-weight:600;color:var(--teal);font-size:40px;line-height:1;letter-spacing:.5px;text-transform:uppercase}
  .card--front .brand{left:106px;top:100px}
  .card--back .brand{left:111px;top:40px}

  .front__web{position:absolute;left:0;right:0;top:232px;text-align:center;color:var(--teal);font-size:20px;letter-spacing:4.5px}
  .front__saying{position:absolute;left:0;right:0;top:274px;text-align:center;color:var(--teal);font-family:'EB Garamond',serif;font-weight:500;font-size:17px;letter-spacing:2px;text-transform:uppercase}

  .band-light{position:absolute;left:0;right:0;top:175px;height:74px;background:var(--sage)}
  .band-dark-left{position:absolute;left:0;width:300px;top:249px;bottom:0;background:var(--teal)}
  .band-dark-right{position:absolute;left:290px;right:0;top:210px;bottom:0;background:var(--teal)}
  .portrait{position:absolute;left:256px;top:167px;width:80px;height:80px;border-radius:50%;background:var(--sage);border:3px solid var(--white)}

  .person{position:absolute;left:0;width:262px;top:186px;text-align:center;color:var(--teal);font-family:'EB Garamond',serif}
  .person__name{font-weight:600;font-size:21px;letter-spacing:.3px;text-transform:uppercase}
  .person__title{font-weight:400;font-size:19px;text-transform:uppercase;margin-top:4px}

  .address{position:absolute;left:24px;top:268px;color:var(--white);font-size:15px;line-height:23px}
  .address__line{display:flex;align-items:center;gap:5px}
  .address__line--indent{padding-left:18px}
  .address__saying{margin-top:6px;font-family:'EB Garamond',serif;font-size:15px;letter-spacing:1.2px;text-transform:uppercase;color:var(--sage)}

  .contacts{position:absolute;left:342px;top:225px;list-style:none;color:var(--white);font-size:15px}
  .contacts li{display:flex;align-items:center;gap:6px;height:27.5px;white-space:nowrap}
  .icon{width:13px;height:13px;flex:none}
</style>
</head>
<body>

<section class="card card--front">
  <div class="brand">
    <span class="brand__mark"></span>
    <span class="brand__name">Holvaster<br>Building Inc.</span>
  </div>
  <p class="front__web">www.holvaster-example.com</p>
  <p class="front__saying">Professional. Quality. Service.</p>
</section>

<section class="card card--back">
  <div class="brand">
    <span class="brand__mark"></span>
    <span class="brand__name">Holvaster<br>Building Inc.</span>
  </div>

  <div class="band-light"></div>
  <div class="band-dark-left"></div>
  <div class="band-dark-right"></div>
  <div class="portrait" role="img" aria-label="Employee portrait photo"></div>

  <div class="person">
    <p class="person__name">Daniel Corvath</p>
    <p class="person__title">President</p>
  </div>

  <div class="address">
    <p class="address__line">
      <svg class="icon" viewBox="0 0 14 14" fill="none" stroke="#fff" stroke-width="1.3"><circle cx="7" cy="7" r="5.8"/><circle cx="7" cy="6" r="1.8"/><path d="M7 8v3"/></svg>
      18 North Tamlin Glen Road, Unit 57
    </p>
    <p class="address__line address__line--indent">Marbrook Vale, ON, K7T 2R9</p>
    <p class="address__saying">Professional. Quality. Service.</p>
  </div>

  <ul class="contacts">
    <li>
      <svg class="icon" viewBox="0 0 14 14" fill="none" stroke="#fff" stroke-width="1.3"><circle cx="7" cy="7" r="5.8"/><path d="M5 4.2c-.8.6-.6 2 .6 3.4s2.6 2 3.4 1.4l-.9-1.2-.9.4-1.6-1.8.4-.9z" fill="#fff"/></svg>
      905-218-5937
    </li>
    <li>
      <svg class="icon" viewBox="0 0 14 14" fill="none" stroke="#fff" stroke-width="1.4"><rect x="3.5" y="1" width="7" height="12" rx="1.3"/><path d="M6 11h2"/></svg>
      905-441-7026
    </li>
    <li>
      <svg class="icon" viewBox="0 0 14 14" fill="none" stroke="#fff" stroke-width="1.3"><path d="M1.5 6 7 2.5 12.5 6v6h-11z"/><path d="M1.5 6 7 9.5 12.5 6"/></svg>
      office@holvaster-example.com
    </li>
    <li>
      <svg class="icon" viewBox="0 0 14 14" fill="none" stroke="#fff" stroke-width="1.1"><circle cx="7" cy="7" r="5.8"/><ellipse cx="7" cy="7" rx="2.5" ry="5.8"/><path d="M1.2 7h11.6M2 4h10M2 10h10"/></svg>
      www.holvaster-example.com
    </li>
  </ul>
</section>

</body>
</html>
```